Bidmark Display ads for Real Estate Photography

I'm looking for someone to take ideas off of my flyers and website (lensvale.example) to create two sets of display ads. One for branding and another for specific specials (see magazine-ad-special.pdf). I would like these to be animated gifs that cycle between 2 or 3 views. Here are the dimensions for the ads:
300 x 250 – Inline Rectangle
728 x 90 – Leaderboard
160 x 600 – Wide Skyscraper
320×100 - Large Mobile Banner
I can also provide source artwork from the flyers if needed.
Target Market(s)
Realtors that sell high end luxury homes
Industry/Entity Type
Professional Photography
Requirements
Must have
- .psd source files for each size ad with screens/views on different layers to I can export as an animated gif
- display ads in the following sizes:
- 300 x 250 – Inline Rectangle
- 728 x 90 – Leaderboard
- 160 x 600 – Wide Skyscraper
- 320×100 - Large Mobile Banner
Nice to have
- 336 x 280 – Large Rectangle
- 300 x 600 – Half-Page Ad

```html
<!DOCTYPE html>
<html lang="en">
<head>
<meta charset="utf-8">
<title>Lensvale – Bidmark Display Ad Set</title>
<link href="https://fonts.googleapis.com/css2?family=Lato:wght@400;700;900&display=swap" rel="stylesheet">
<style>
  :root{
    --board:#5d5d5d;
    --sky:#2b8fc8;
    --deep:#0c5aa8;
    --ink:#ffffff;
    --corner:#e8f0f5;
    --button:#575757;
    --photo-a:#c9ccc9;
    --photo-b:#8a8f8c;
    --pool:#2a7fb8;
    --logo:#0b5aa6;
  }
  *{margin:0;padding:0;box-sizing:border-box}
  html,body{width:1200px;height:1200px;overflow:hidden;background:var(--board)}
  body{position:relative;font-family:"Lato",sans-serif}
  .ad{position:absolute;display:block}
  .ad-label{position:absolute;color:var(--ink);font-size:18px;font-weight:400;white-space:nowrap;transform:translateX(-50%)}
  .headline{fill:var(--ink);font-family:"Lato",sans-serif;font-weight:700}
  .brand{fill:var(--logo);font-family:"Lato",sans-serif;font-weight:900}
  .cta-bg{fill:var(--button)}
  .cta-text{fill:var(--ink);font-family:"Lato",sans-serif;font-weight:700}
  .sky{fill:var(--sky)}
  .deep{fill:var(--deep)}
  .corner{fill:var(--corner)}
  .ring{fill:none;stroke:#fff;stroke-width:4}
</style>
</head>
<body>

<svg class="ad ad-half-page" style="left:74px;top:238px" width="240" height="480" viewBox="0 0 300 600">
  <defs>
    <linearGradient id="room" x1="0" y1="0" x2="0" y2="1"><stop offset="0" stop-color="#9fb0b8"/><stop offset=".6" stop-color="#d8d6cf"/><stop offset="1" stop-color="#c9c1b2"/></linearGradient>
    <linearGradient id="pool" x1="0" y1="0" x2="0" y2="1"><stop offset="0" stop-color="#8a6a52"/><stop offset="1" stop-color="#2a8fd0"/></linearGradient>
  </defs>
  <rect role="img" aria-label="Bright white luxury kitchen with island and pendant lights" width="300" height="290" fill="url(#room)"/>
  <rect class="sky" y="270" width="300" height="330"/>
  <path class="deep" d="M0 270 C120 270 230 240 300 190 L300 230 C220 290 120 310 0 312 Z"/>
  <path class="corner" d="M300 525 C270 560 240 585 200 600 L300 600 Z"/>
  <rect fill="#fff" width="150" height="85"/>
  <circle cx="8" cy="40" r="5" class="brand"/>
  <text class="brand" x="18" y="54" font-size="36">Lensvale</text>
  <circle role="img" aria-label="Pool courtyard at dusk" cx="121" cy="289" r="48" fill="url(#pool)"/>
  <circle class="ring" cx="121" cy="289" r="48"/>
  <circle role="img" aria-label="Kitchen detail" cx="223" cy="250" r="55" fill="url(#room)"/>
  <circle class="ring" cx="223" cy="250" r="55"/>
  <text class="headline" x="24" y="385" font-size="34">GROW YOUR</text>
  <text class="headline" x="24" y="425" font-size="34">BUSINESS</text>
  <text class="headline" x="24" y="465" font-size="34">&amp; SELL MORE</text>
  <text class="headline" x="24" y="505" font-size="34">HOMES</text>
  <rect class="cta-bg" x="70" y="536" width="120" height="34" rx="17"/>
  <text class="cta-text" x="130" y="560" font-size="20" text-anchor="middle">Learn More</text>
</svg>
<div class="ad-label" style="left:193px;top:743px">300 x 600 – Half-Page Ad</div>

<svg class="ad ad-skyscraper" style="left:392px;top:240px" width="128" height="480" viewBox="0 0 160 600">
  <rect role="img" aria-label="Bright white luxury kitchen" width="160" height="290" fill="url(#room)"/>
  <rect class="sky" y="270" width="160" height="330"/>
  <path class="deep" d="M0 268 C60 268 120 250 160 215 L160 250 C110 290 60 300 0 300 Z"/>
  <path class="corner" d="M160 520 C145 560 130 585 105 600 L160 600 Z"/>
  <rect fill="#fff" width="105" height="60"/>
  <circle cx="6" cy="30" r="4" class="brand"/>
  <text class="brand" x="13" y="40" font-size="24">Lensvale</text>
  <circle role="img" aria-label="Pool courtyard at dusk" cx="39" cy="300" r="35" fill="url(#pool)"/>
  <circle class="ring" cx="39" cy="300" r="35"/>
  <circle role="img" aria-label="Kitchen detail" cx="114" cy="266" r="42" fill="url(#room)"/>
  <circle class="ring" cx="114" cy="266" r="42"/>
  <g text-anchor="middle">
    <text class="headline" x="80" y="374" font-size="21">GROW YOUR</text>
    <text class="headline" x="80" y="399" font-size="21">BUSINESS</text>
    <text class="headline" x="80" y="431" font-size="21">&amp;</text>
    <text class="headline" x="80" y="466" font-size="21">SELL MORE</text>
    <text class="headline" x="80" y="491" font-size="21">HOMES</text>
    <rect class="cta-bg" x="32" y="513" width="100" height="32" rx="16"/>
    <text class="cta-text" x="82" y="535" font-size="16">Learn More</text>
  </g>
</svg>
<div class="ad-label" style="left:455px;top:745px">160 x 600 – Wide Skyscraper</div>

<svg class="ad ad-large-rect" style="left:615px;top:498px" width="269" height="224" viewBox="0 0 336 280">
  <rect role="img" aria-label="Bright white luxury kitchen" width="336" height="160" fill="url(#room)"/>
  <rect class="sky" y="150" width="336" height="130"/>
  <path class="deep" d="M0 150 C140 150 260 130 336 70 L336 105 C250 170 130 195 0 195 Z"/>
  <path class="corner" d="M336 215 C310 250 280 270 240 280 L336 280 Z"/>
  <rect fill="#fff" width="115" height="55"/>
  <circle cx="6" cy="26" r="4" class="brand"/>
  <text class="brand" x="13" y="36" font-size="26">Lensvale</text>
  <circle role="img" aria-label="Kitchen detail" cx="260" cy="148" r="65" fill="url(#room)"/>
  <circle class="ring" cx="260" cy="148" r="65"/>
  <text class="headline" x="14" y="218" font-size="17">GROW YOUR</text>
  <text class="headline" x="14" y="238" font-size="17">BUSINESS</text>
  <text class="headline" x="14" y="258" font-size="17">&amp; SELL MORE HOMES</text>
  <rect class="cta-bg" x="215" y="242" width="98" height="22" rx="11"/>
  <text class="cta-text" x="264" y="257" font-size="11" text-anchor="middle">Learn More</text>
</svg>
<div class="ad-label" style="left:747px;top:745px">336 x 280 – Large Rectangle</div>

<svg class="ad ad-inline-rect" style="left:928px;top:518px" width="240" height="200" viewBox="0 0 300 250">
  <rect role="img" aria-label="Bright white luxury kitchen" width="300" height="135" fill="url(#room)"/>
  <rect class="sky" y="125" width="300" height="125"/>
  <path class="deep" d="M0 122 C120 122 230 100 300 55 L300 90 C220 140 120 160 0 160 Z"/>
  <path class="corner" d="M300 205 C285 228 265 242 240 250 L300 250 Z"/>
  <rect fill="#fff" width="100" height="45"/>
  <circle cx="5" cy="22" r="3.5" class="brand"/>
  <text class="brand" x="11" y="31" font-size="22">Lensvale</text>
  <circle role="img" aria-label="Kitchen detail" cx="227" cy="124" r="58" fill="url(#room)"/>
  <circle class="ring" cx="227" cy="124" r="58"/>
  <text class="headline" x="7" y="183" font-size="21">GROW YOUR</text>
  <text class="headline" x="7" y="208" font-size="21">BUSINESS &amp;</text>
  <text class="headline" x="7" y="233" font-size="21">SELL MORE HOMES</text>
  <rect class="cta-bg" x="205" y="214" width="88" height="22" rx="11"/>
  <text class="cta-text" x="249" y="229" font-size="11" text-anchor="middle">Learn More</text>
</svg>
<div class="ad-label" style="left:1047px;top:745px">300 x 250 – Inline Rectangle</div>

<svg class="ad ad-leaderboard" style="left:75px;top:818px" width="582" height="72" viewBox="0 0 728 90">
  <rect role="img" aria-label="Bright white luxury kitchen" width="330" height="90" fill="url(#room)"/>
  <path class="sky" d="M310 0 L728 0 L728 90 L265 90 C290 60 300 30 310 0 Z"/>
  <path class="deep" d="M290 0 L318 0 C305 35 290 65 268 90 L250 90 C270 65 283 35 290 0 Z"/>
  <path class="corner" d="M706 0 L728 0 L728 90 L666 90 C685 65 698 35 706 0 Z"/>
  <rect fill="#fff" width="85" height="45"/>
  <circle cx="5" cy="22" r="3.5" class="brand"/>
  <text class="brand" x="11" y="31" font-size="19">Lensvale</text>
  <g text-anchor="middle">
    <text class="headline" x="490" y="24" font-size="20">GROW YOUR BUSINESS &amp; SELL</text>
    <text class="headline" x="490" y="49" font-size="20">MORE HOMES</text>
    <rect class="cta-bg" x="443" y="64" width="90" height="18" rx="9"/>
    <text class="cta-text" x="488" y="77" font-size="11">Learn More</text>
  </g>
</svg>
<div class="ad-label" style="left:362px;top:912px">728 x 90 – Leaderboard</div>

<svg class="ad ad-mobile-banner" style="left:774px;top:811px" width="256" height="80" viewBox="0 0 320 100">
  <rect role="img" aria-label="Bright white luxury kitchen" width="200" height="100" fill="url(#room)"/>
  <path class="sky" d="M185 0 L320 0 L320 100 L160 100 C172 70 180 35 185 0 Z"/>
  <path class="deep" d="M172 0 L190 0 C185 35 175 70 162 100 L148 100 C160 70 168 35 172 0 Z"/>
  <path class="corner" d="M314 0 L320 0 L320 100 L272 100 C292 70 306 35 314 0 Z"/>
  <rect fill="#fff" width="78" height="42"/>
  <circle cx="5" cy="21" r="3.5" class="brand"/>
  <text class="brand" x="11" y="29" font-size="17">Lensvale</text>
  <text class="headline" x="185" y="15" font-size="12">GROW YOUR</text>
  <text class="headline" x="185" y="30" font-size="12">BUSINESS</text>
  <text class="headline" x="185" y="45" font-size="12">&amp; SELL MORE</text>
  <text class="headline" x="185" y="60" font-size="12">HOMES</text>
  <rect class="cta-bg" x="174" y="76" width="78" height="17" rx="8.5"/>
  <text class="cta-text" x="213" y="88" font-size="11" text-anchor="middle">Learn More</text>
</svg>
<div class="ad-label" style="left:902px;top:911px">320×100 - Large Mobile Banner</div>

</body>
</html>
```